Stationery for Wellness Business -

Need Envelopes, Letter Head Paper, Perhaps Note Pad and Business Cards. Logo Already established and is attached. Catch phrase is the following: Cultivating sound minds, bodies and spirits. Colors of business is below as well. Address of business: 18462 Larchmont Avenue, Suite 215, Alder Falls, Indiana 44187, USA.
website: https://www.stillbrookhaven.com/
email: stillbrookhaven@thedeskwizards.ai
phone: 1.650.555.0148

Business Card Info: Daniel Whitford, MD. Founder & CEO
dr.whitford@stillbrookhaven.com
1.650.555.0148 office, cell 814.555.0193

prefer the green colors of SBH primary Color Palette with accents from the other colors. overall style zen, minimalist, calm, but modern and professional in tone.

```html
<!DOCTYPE html>
<html lang="en">
<head>
<meta charset="utf-8">
<title>Stillbrook Haven Stationery</title>
<link href="https://fonts.googleapis.com/css2?family=Montserrat:wght@400;500;700&family=Lato:wght@400;700&family=Tangerine:wght@700&display=swap" rel="stylesheet">
<style>
  :root{
    --backdrop:#a6a6a6;
    --paper:#ffffff;
    --sage:#3f5a2a;
    --ink:#1d1d1d;
    --rule:#555555;
  }
  *{margin:0;padding:0;box-sizing:border-box}
  html,body{width:1200px;height:946px;overflow:hidden;background:var(--backdrop)}
  .canvas{position:relative;width:1200px;height:946px}
  .sheet{position:absolute;background:var(--paper);box-shadow:2px 3px 5px rgba(0,0,0,.45)}
  .mark{position:absolute;border:1px solid var(--sage);border-radius:50%}
  .brand{position:absolute;font-family:'Montserrat',sans-serif;font-weight:500;color:var(--sage);text-transform:uppercase;white-space:nowrap;text-align:center}

  /* business card front */
  .card-front{left:68px;top:85px;width:316px;height:180px}
  .card-front .mark{left:114px;top:44px;width:87px;height:87px;border-width:1.5px}
  .card-front .brand{left:0;right:0;top:134px;font-size:16px;letter-spacing:2px}

  /* business card back */
  .card-back{left:68px;top:290px;width:316px;height:180px}
  .card-back .mark{left:55px;top:65px;width:46px;height:46px;border-width:1.2px}
  .card-back .brand{left:20px;width:116px;top:113px;font-size:8px;letter-spacing:.8px}
  .card-back .divider{position:absolute;left:141px;top:56px;width:1.2px;height:68px;background:var(--sage)}
  .card-back .person{position:absolute;left:154px;top:53px;font-family:'Montserrat',sans-serif;color:var(--sage)}
  .person .name{font-size:13px;font-weight:700;letter-spacing:.1px}
  .person .role{font-size:8.6px;color:#333;margin-top:3px}
  .person .contacts{list-style:none;margin-top:9px;font-size:8.5px;color:#333}
  .person .contacts li{display:flex;align-items:center;gap:4px;height:12.5px}
  .person svg{width:7px;height:7px;fill:var(--sage)}

  /* letterhead */
  .letterhead{left:409px;top:87px;width:270px;height:382px;font-family:'Lato',sans-serif;color:var(--ink)}
  .letterhead .mark{left:36px;top:13px;width:37px;height:37px}
  .letterhead .brand{left:6px;width:98px;top:57px;font-size:6px;letter-spacing:.5px}
  .letterhead .divider{position:absolute;left:152px;top:23px;width:.8px;height:34px;background:var(--sage)}
  .letterhead .address{position:absolute;left:164px;top:21px;font-family:'Montserrat',sans-serif;font-size:4.6px;line-height:6.2px;color:#333}
  .address .gap{height:4px}
  .letter{position:absolute;left:13px;top:97px;width:244px;font-size:5.6px;line-height:6.1px}
  .letter .date{font-size:5.8px}
  .letter .recipient{margin-top:7px}
  .letter .company{margin-top:11px}
  .letter .salute{margin-top:13px;font-size:7px;font-weight:700}
  .letter .body p{margin-top:6px;text-align:justify;font-size:5.1px;line-height:5.9px}
  .letter .body p:first-child{margin-top:12px}
  .letter .regards{margin-top:12px}
  .letter .signature{margin-top:14px;font-family:'Tangerine',cursive;font-size:17px;line-height:15px;color:var(--ink)}

  /* envelope front */
  .envelope-front{left:704px;top:89px;width:399px;height:173px}
  .envelope-front .mark{left:27px;top:18px;width:17px;height:17px}
  .envelope-front .brand{left:10px;width:52px;top:36px;font-size:3.6px;letter-spacing:.2px}
  .envelope-front .divider{position:absolute;left:63px;top:16px;width:.9px;height:24px;background:var(--sage)}
  .envelope-front .address{position:absolute;left:71px;top:19px;font-family:'Montserrat',sans-serif;font-size:6.6px;line-height:8.2px;color:#333}

  /* envelope back */
  .envelope-back{left:699px;top:290px;width:401px;height:176px}
  .envelope-back .flap{position:absolute;left:0;top:0;width:401px;height:64px}
  .envelope-back .mark{left:186px;top:10px;width:30px;height:30px;border-color:#fff}
  .envelope-back .brand{left:150px;width:101px;top:44px;font-size:5px;letter-spacing:.5px;color:#fff}

  /* notepad */
  .notepad{left:855px;top:522px;width:208px;height:297px}
  .notepad .mark{left:21px;top:11px;width:17px;height:17px}
  .notepad .brand{left:4px;width:52px;top:30px;font-size:3.6px;letter-spacing:.2px}
  .notepad .date{position:absolute;right:9px;top:17px;font-family:'Lato',sans-serif;font-size:6.8px;color:#222}
  .notepad .lines{position:absolute;left:10px;top:53px;width:188px;list-style:none}
  .notepad .lines li{height:11.6px;border-top:.8px solid var(--rule)}
</style>
</head>
<body>
<main class="canvas">

  <section class="sheet card-front">
    <span class="mark"></span>
    <span class="brand">Stillbrook Haven</span>
  </section>

  <section class="sheet card-back">
    <span class="mark"></span>
    <span class="brand">Stillbrook Haven</span>
    <span class="divider"></span>
    <div class="person">
      <p class="name">Daniel Whitford, MD.</p>
      <p class="role">Founder &amp; CEO</p>
      <ul class="contacts">
        <li><svg viewBox="0 0 10 10"><path d="M1 4c0-2 2-3 4-3s4 1 4 3H7L6.5 3h-3L3 4zM2 5h6l1 4H1z"/></svg>1.650.555.0148</li>
        <li><svg viewBox="0 0 10 10"><path d="M3 0h4a1 1 0 0 1 1 1v8a1 1 0 0 1-1 1H3a1 1 0 0 1-1-1V1a1 1 0 0 1 1-1zm0 1.5v6h4v-6z"/></svg>814.555.0193</li>
        <li><svg viewBox="0 0 10 10"><path d="M0 2h10v1L5 6 0 3zM0 4l5 3 5-3v4H0z"/></svg>dr.whitford@stillbrookhaven.com</li>
      </ul>
    </div>
  </section>

  <section class="sheet letterhead">
    <span class="mark"></span>
    <span class="brand">Stillbrook Haven</span>
    <span class="divider"></span>
    <div class="address">
      <p>18462 Larchmont Avenue, Suite 215,</p>
      <p>Alder Falls, Indiana 44187, USA.</p>
      <div class="gap"></div>
      <p>&#9742; 1.650.555.0148</p>
      <p>&#9993; stillbrookhaven@thedeskwizards.ai</p>
      <p>&#9679; www.stillbrookhaven.com</p>
    </div>
    <article class="letter">
      <p class="date">January-03-2020</p>
      <p class="recipient">Mr, Alan Reyes<br>President</p>
      <p class="company">Harbor Lane Group<br>123 Street Name, Suite# 10<br>City, State, 120023</p>
      <p class="salute">Dear Mr, Alan</p>
      <div class="body">
        <p>Lorem ipsum dolor sit amet, consectetur adipiscing elit, sed do eiusmod tempor incididunt ut labore et dolore magna aliqua. Ut enim ad minim veniam, quis nostrud exercitation ullamco laboris nisi ut aliquip ex ea commodo consequat. Duis aute irure dolor in reprehenderit in voluptate velit esse cillum dolore eu fugiat nulla pariatur.</p>
        <p>Lorem ipsum dolor sit amet, consectetur adipiscing elit, sed do eiusmod tempor incididunt ut labore et dolore magna aliqua. Ut enim ad minim veniam, quis nostrud exercitation ullamco laboris nisi ut aliquip ex ea commodo consequat. Duis aute irure dolor in reprehenderit in voluptate velit esse cillum dolore eu fugiat nulla pariatur.</p>
        <p>Lorem ipsum dolor sit amet, consectetur adipiscing elit, sed do eiusmod tempor incididunt ut labore et dolore magna aliqua. Ut enim ad minim veniam, quis nostrud exercitation ullamco laboris nisi ut aliquip ex ea commodo consequat.</p>
        <p>Excepteur sint occaecat cupidatat non proident, sunt in culpa qui officia deserunt mollit anim id est laborum. re et dolore magnam aliquam quaerat voluptatem.</p>
      </div>
      <p class="regards">Regards</p>
      <p class="signature">Elena Marsh</p>
    </article>
  </section>

  <section class="sheet envelope-front">
    <span class="mark"></span>
    <span class="brand">Stillbrook Haven</span>
    <span class="divider"></span>
    <div class="address">
      <p>18462 Larchmont Avenue, Suite 215,</p>
      <p>Alder Falls, Indiana 44187, USA.</p>
    </div>
  </section>

  <section class="sheet envelope-back">
    <svg class="flap" viewBox="0 0 401 64" aria-hidden="true">
      <path d="M0 0H401L387 48Q383 64 366 64H35Q18 64 14 48Z" fill="var(--sage)"/>
    </svg>
    <span class="mark"></span>
    <span class="brand">Stillbrook Haven</span>
  </section>

  <section class="sheet notepad">
    <span class="mark"></span>
    <span class="brand">Stillbrook Haven</span>
    <p class="date">Date......./....../.......</p>
    <ul class="lines">
      <li></li><li></li><li></li><li></li><li></li><li></li><li></li><li></li><li></li><li></li>
      <li></li><li></li><li></li><li></li><li></li><li></li><li></li><li></li><li></li><li></li>
    </ul>
  </section>

</main>
</body>
</html>
```